Dog breeder design card

A card for our dog showing/breeding and companion puppy buyers.
Updates

Reason: The photo's I provided were not seen by designers because of a glitch or error, so I will need to start them over again in the designs submitted to me. I uploaded and emailed the photo's last night.

Thank you all so much for your lovely designs, I like wquite a few of them. I provided images in my original brief, but these apparently did not become available for you to see. I have emailed my images now, so hopefully you may be able to incorporate them into your designs.

Thank you so much for your time,
kind regards,
Beatrice

I have attached the photo’s that can hopefully be incorporated onto my business card. I don’t mind if the whole images aren’t used, but maybe a soft focus look around the adult dog and in a corner of the card maybe....if that’s possible.

Contact Information for Business Card

Corvanel Bullmastiffs, adored by Gerald and Beatrice Lindqvist.
Cranebrook NSW
0478 552961

Requirements
Nice to have
• Soft focus look to the outline of adult dogs head incorporated into perhaps a corner of the card. Soft focus outline around pups perhaps.
I do really love hot pink and/or purple text if possible.
"Corvanel Bullmastiffs" to be incorporated on the front of card, our details on reverse.
Would prefer a glossy finish rather than matt.

```html
<!DOCTYPE html>
<html lang="en">
<head>
<meta charset="utf-8">
<title>Corvanel Bullmastiffs – Card Front</title>
<link rel="stylesheet" href="https://fonts.googleapis.com/css2?family=Exo:wght@600&family=Arimo&display=swap">
<style>
  :root {
    --page-bg: #ffffff;
    --frame-red: #c8102e;
    --card-purple: #6e2a8c;
    --wave-purple: #7a2892;
    --band-pink: #b0448e;
    --glow: #9a30c0;
    --name-pink: #d9508f;
    --name-white: #ffffff;
    --url-grey: #d2c6dc;
    --pup-tan: #e6cfae;
    --pup-dark: #3b2a24;
  }
  html, body {
    margin: 0;
    padding: 0;
    width: 1200px;
    height: 741px;
    overflow: hidden;
    background: var(--page-bg);
  }
  .canvas {
    position: relative;
    width: 1200px;
    height: 741px;
  }
  .presentation-frame {
    position: absolute;
    left: 16px;
    top: 16px;
    width: 1162px;
    height: 701px;
    border: 3px solid var(--frame-red);
  }
  .card {
    position: absolute;
    left: 41px;
    top: 41px;
    width: 1119px;
    height: 657px;
    overflow: hidden;
    background: var(--card-purple);
  }
  .card-background {
    position: absolute;
    inset: 0;
    width: 100%;
    height: 100%;
  }
  .puppy-photo {
    position: absolute;
    left: 519px;
    top: 219px;
    width: 210px;
    height: 156px;
    border-radius: 40%;
    background: radial-gradient(ellipse at 50% 55%, var(--pup-tan) 0%, #cdb08e 45%, rgba(154, 48, 192, 0) 75%);
  }
  .brand-name {
    position: absolute;
    left: 281px;
    top: 360px;
    width: 600px;
    margin: 0;
    text-align: center;
    font-family: "Exo", sans-serif;
    font-weight: 600;
    font-size: 47px;
    line-height: 1;
    letter-spacing: 0.5px;
    white-space: nowrap;
  }
  .brand-name .first-word { color: var(--name-pink); }
  .brand-name .second-word { color: var(--name-white); }
  .web-address {
    position: absolute;
    left: 254px;
    top: 411px;
    width: 600px;
    margin: 0;
    text-align: center;
    font-family: "Arimo", sans-serif;
    font-size: 13px;
    color: var(--url-grey);
  }
</style>
</head>
<body>
<div class="canvas">
  <div class="presentation-frame"></div>
  <section class="card">
    <svg class="card-background" viewBox="0 0 1119 657" preserveAspectRatio="none" aria-hidden="true">
      <defs>
        <radialGradient id="centerGlow" cx="0.55" cy="0.42" r="0.3">
          <stop offset="0" stop-color="var(--glow)" stop-opacity="0.7"/>
          <stop offset="1" stop-color="var(--glow)" stop-opacity="0"/>
        </radialGradient>
      </defs>
      <rect class="top-band" x="0" y="0" width="1119" height="200" fill="var(--band-pink)"/>
      <rect class="bottom-band" x="0" y="460" width="1119" height="197" fill="var(--band-pink)"/>
      <path class="wave-top-outer" fill="var(--wave-purple)"
        d="M0 72 C120 60 220 110 340 112 C480 114 560 66 720 68 C860 70 930 112 1030 110 C1070 108 1100 96 1119 88 L1119 580 L0 580 Z"/>
      <path class="wave-top-inner" fill="var(--card-purple)"
        d="M0 100 C120 92 220 140 340 142 C480 144 560 98 720 100 C860 102 930 140 1030 138 C1070 136 1100 126 1119 118 L1119 560 L0 560 Z"/>
      <path class="wave-bottom-outer" fill="var(--wave-purple)"
        d="M0 520 C140 516 240 552 380 554 C520 556 640 520 760 522 C880 524 960 556 1119 550 L1119 590 C960 596 880 564 760 562 C640 560 520 596 380 594 C240 592 140 556 0 560 Z"/>
      <path class="wave-bottom-band" fill="var(--band-pink)"
        d="M0 560 C140 556 240 592 380 594 C520 596 640 560 760 562 C880 564 960 596 1119 590 L1119 657 L0 657 Z"/>
      <rect x="0" y="0" width="1119" height="657" fill="url(#centerGlow)"/>
    </svg>
    <div class="puppy-photo" role="img" aria-label="Photo of two fawn bullmastiff puppies lying side by side"></div>
    <h1 class="brand-name"><span class="first-word">Corvanel</span> <span class="second-word">Bullmastiffs</span></h1>
    <p class="web-address">www.Corvanel Bullmastiffs.com</p>
  </section>
</div>
</body>
</html>
```